Buisness card

**Front Side:**

**[Your Company Logo]**
**Steadfast Upkeep Industrial**
*Keeping Your Equipment Running Smoothly*

**Contact Information:**
- **Name:** [darren Whitlow
- **Title:** [owner
- **Phone:** [8025196047
- **Email:** darren@sukrn.com

**Back Side:**

**Services Offered:**
- Routine Inspections
- Equipment Maintenance
- Emergency Repairs
- Consultation Services
- New installs
Tag line
Be proactive not reactive

```html
<!DOCTYPE html>
<html lang="en">
<head>
<meta charset="utf-8">
<title>Steadfast Upkeep Industrial – Business Card</title>
<link rel="stylesheet" href="https://fonts.googleapis.com/css2?family=Arimo:wght@400;700&display=swap">
<style>
  :root {
    --navy: #002a6e;
    --sky: #00c8fb;
    --white: #ffffff;
    --accent-blue: #1f6dff;
    --ink: #0d1a3a;
    --backdrop: #e6e6e6;
  }
  * { margin: 0; padding: 0; box-sizing: border-box; }
  html, body { width: 1200px; height: 1200px; overflow: hidden; }
  body {
    background: var(--backdrop);
    font-family: "Arimo", Arial, sans-serif;
    position: relative;
  }
  .card {
    position: absolute;
    left: 256px;
    width: 688px;
    height: 393px;
    background: var(--white);
    overflow: hidden;
  }
  .card--front { top: 159px; }
  .card--back { top: 653px; }
  .card__art { position: absolute; inset: 0; width: 688px; height: 393px; }

  .contact { position: absolute; left: 57px; top: 124px; color: var(--white); }
  .contact__name {
    font-size: 27px; font-weight: 700; color: var(--accent-blue); line-height: 1;
  }
  .contact__title { font-size: 15.5px; margin-top: 6px; }
  .contact__list { list-style: none; margin-top: 30px; }
  .contact__item {
    display: flex; align-items: center; font-size: 16px; height: 20.5px;
  }
  .contact__icon { width: 14px; height: 14px; margin-right: 12px; flex: none; }

  .brand-name {
    color: var(--navy);
    font-weight: 700;
    text-align: center;
    line-height: 1.1;
  }
  .card--front .brand-name {
    position: absolute;
    left: 484px; top: 175px; width: 140px; font-size: 15px;
  }
  .brand-label {
    position: absolute;
    left: 259px; top: 140px; width: 292px; height: 70px;
    background: var(--white); border-radius: 6px;
    padding: 0 8px;
    display: flex; flex-direction: column; align-items: center; justify-content: center;
    gap: 6px;
  }
  .brand-label .brand-name { font-size: 19px; white-space: nowrap; }
  .brand-label__motto {
    font-size: 14.5px; font-weight: 700; color: var(--ink);
    letter-spacing: 0.2px; white-space: nowrap; line-height: 1;
  }
  .tagline {
    position: absolute; left: 0; right: 0; top: 352px;
    text-align: center; color: var(--accent-blue); font-size: 16.5px;
  }
</style>
</head>
<body>

<section class="card card--front">
  <svg class="card__art" viewBox="0 0 688 393" aria-hidden="true">
    <rect x="0" y="0" width="688" height="334" fill="var(--navy)"/>
    <polygon points="0,0 88,0 0,188" fill="var(--white)"/>
    <polygon points="638,0 688,0 688,334 482,334" fill="var(--sky)"/>
    <circle cx="554" cy="199" r="80" fill="var(--white)"/>
  </svg>
  <div class="brand-name">Steadfast Upkeep Industrial</div>

  <div class="contact">
    <h1 class="contact__name">darren Whitlow</h1>
    <p class="contact__title">Owner</p>
    <ul class="contact__list">
      <li class="contact__item">
        <svg class="contact__icon" viewBox="0 0 24 24"><path fill="var(--accent-blue)" d="M6.6 10.8a15.1 15.1 0 0 0 6.6 6.6l2.2-2.2c.3-.3.7-.4 1-.2 1.1.4 2.3.6 3.6.6.6 0 1 .4 1 1V20c0 .6-.4 1-1 1C10.6 21 3 13.4 3 4c0-.6.4-1 1-1h3.5c.6 0 1 .4 1 1 0 1.3.2 2.5.6 3.6.1.3 0 .7-.2 1z"/></svg>
        8025196047
      </li>
      <li class="contact__item">
        <svg class="contact__icon" viewBox="0 0 24 24"><rect x="2" y="5" width="20" height="14" fill="var(--accent-blue)"/><path d="M2 5l10 8 10-8" fill="none" stroke="var(--navy)" stroke-width="2"/></svg>
        darren@sukrn.com
      </li>
      <li class="contact__item">
        <svg class="contact__icon" viewBox="0 0 24 24"><circle cx="12" cy="12" r="10" fill="var(--accent-blue)"/><path d="M2 12h20M12 2c3 3 3 17 0 20M12 2c-3 3-3 17 0 20" fill="none" stroke="var(--navy)" stroke-width="1.5"/></svg>
        www.sukrn.com
      </li>
    </ul>
  </div>
</section>

<section class="card card--back">
  <svg class="card__art" viewBox="0 0 688 393" aria-hidden="true">
    <rect x="0" y="0" width="688" height="333" fill="var(--sky)"/>
    <polygon points="0,0 434,0 279,333 0,333" fill="var(--navy)"/>
    <circle cx="198" cy="175" r="63" fill="var(--white)"/>
  </svg>
  <div class="brand-label">
    <div class="brand-name">Steadfast Upkeep Industrial</div>
    <div class="brand-label__motto">BE PROACTIVE NOT REACTIVE</div>
  </div>
  <p class="tagline">Keeping Your Equipment Running Smoothly*</p>
</section>

</body>
</html>
```